ORLUq Business card. A.I. company developing trading strategies.

My name is tommaso fabbri and I'm CEO and co-founder of ORLUQ Research, an AI company focusing on generating Ai-driven trading strategies.
This is our website: https://orluq-research.example/
Values of our company: tech & R&D driven (we're all very mathy/stats/data driven), sophisticated (we only look for sophisticated, high knowledge investors), reserved (we don't go around telling anyone what we do).
Our main product: KobraFNX. A trading strategy that delivered 70% in 2022 and 20% in 2023 so far.
Our main potential clients: HNW individuals, hedge funds, asset managers, tech entrepreneur.
Hedge funds, asset managers, High Net Worth individuals, Pension funds
The basic: name, job title, company name, address, mail, phone number

```html
<!DOCTYPE html>
<html lang="en">
<head>
<meta charset="utf-8">
<title>ORLUq Research – Business Card</title>
<link href="https://fonts.googleapis.com/css2?family=Montserrat:wght@400;500;700&display=swap" rel="stylesheet">
<style>
  :root {
    --backdrop: #3a322d;
    --card: #232325;
    --card-deep: #1c1c1e;
    --panel-shade: #18181a;
    --pattern: #2f3033;
    --ink: #f2f2f2;
    --ink-soft: #d9d9d9;
    --accent: #b61f3c;
  }
  * { box-sizing: border-box; margin: 0; padding: 0; }
  html, body {
    width: 1200px; height: 786px; overflow: hidden;
    background: var(--backdrop);
    font-family: "Montserrat", sans-serif;
  }
  .canvas {
    position: relative; width: 1200px; height: 786px;
    display: flex; align-items: center; justify-content: center; gap: 40px;
  }
  .card {
    position: relative; width: 540px; height: 310px;
    background: var(--card);
    border-radius: 3px;
    overflow: hidden;
    box-shadow: 0 14px 30px rgba(0,0,0,.35);
  }
  .card__pattern {
    position: absolute; inset: 0;
    background: radial-gradient(ellipse at 55% 45%, var(--pattern) 0%, var(--card) 70%);
  }
  .brand {
    position: absolute; display: flex; align-items: center; gap: 10px;
    color: var(--ink); font-weight: 500; white-space: nowrap;
    letter-spacing: .06em;
  }
  .brand__mark {
    width: 9px; height: 9px; background: var(--accent);
  }

  /* back: details */
  .card--back .card__logo-panel {
    position: absolute; left: 0; top: 0; bottom: 0; width: 245px;
    background: var(--card-deep);
    box-shadow: 6px 0 14px rgba(0,0,0,.45);
  }
  .card--back .card__logo-panel .card__pattern {
    background: radial-gradient(ellipse at 50% 50%, var(--pattern) 0%, var(--card-deep) 72%);
  }
  .card--back .brand { left: 34px; top: 145px; font-size: 21px; }

  .details {
    position: absolute; left: 280px; top: 88px; right: 20px;
    color: var(--ink-soft); font-size: 12.5px; line-height: 1.45;
  }
  .details__name { color: var(--accent); font-weight: 700; font-size: 20px; line-height: 1.1; }
  .details__title { margin-bottom: 12px; }
  .details__address { margin-bottom: 14px; }
  .contact { list-style: none; }
  .contact li { display: flex; align-items: center; gap: 10px; }
  .contact svg { width: 11px; height: 11px; flex: none; fill: var(--accent); }

  /* front: logo */
  .card--front .brand { left: 50%; top: 50%; transform: translate(-50%, -50%); font-size: 30px; }
</style>
</head>
<body>
<main class="canvas">

  <section class="card card--back" aria-label="Business card, back">
    <div class="card__logo-panel">
      <div class="card__pattern" role="img" aria-label="Faint circuit-line and wave pattern"></div>
      <div class="brand"><span class="brand__mark"></span>ORLUq Research</div>
    </div>
    <div class="details">
      <p class="details__name">Tommaso Fabbri</p>
      <p class="details__title">CEO and co-founder</p>
      <p class="details__address">14 rue des Lanternes 75004 Paris</p>
      <ul class="contact">
        <li>
          <svg viewBox="0 0 12 12" aria-hidden="true"><path d="M2.5 1h2l1 3-1.3 1a7 7 0 0 0 2.8 2.8L8 6.5l3 1v2a1.5 1.5 0 0 1-1.5 1.5A8.5 8.5 0 0 1 1 2.5 1.5 1.5 0 0 1 2.5 1z"/></svg>
          801 55 0417
        </li>
        <li>
          <svg viewBox="0 0 12 12" aria-hidden="true"><path d="M1 2.5h10v7H1z M1 2.5l5 4 5-4" fill="none" stroke="#b61f3c" stroke-width="1.3"/></svg>
          info@orluq-research.example
        </li>
        <li>
          <svg viewBox="0 0 12 12" aria-hidden="true"><g fill="none" stroke="#b61f3c" stroke-width="1.1"><circle cx="6" cy="6" r="5"/><ellipse cx="6" cy="6" rx="2.2" ry="5"/><path d="M1 6h10"/></g></svg>
          orluq-research.example
        </li>
      </ul>
    </div>
  </section>

  <section class="card card--front" aria-label="Business card, front">
    <div class="card__pattern" role="img" aria-label="Faint circuit-line and wave pattern"></div>
    <div class="brand"><span class="brand__mark"></span>ORLUq Research</div>
  </section>

</main>
</body>
</html>
```